Event Website for the Audio & Visual Industry

Convene is an exhibition aimed at meeting the business needs of audio and visual professionals – the visitors are the ones that make purchase decisions when buying anything to do with AV installation, Lighting & Entertainment Technology, DJ Technologies and even Musical Instruments.

We need to rebuild our website to reflect the professional look but with a bit of creativity/flare that is associated with the industry.

Websites whose design is along the lines we're looking for:

• http:www.fennelbrook.com.au
• http:www.kestral.com
• http://www.brightpanelfair.net/ (competitor expo, like the layout. Not fantastic though, but the best I’ve seen from the industry)
• http://www.vantor.com.au and http://www.halvecrest.com.au/ (Like these brand websites, they are clean and corporate but the use of imagery allows it to have some personality)

Target Market(s)

Corporate AV End Users, Lighting Designers, Concert/Entertainment companies, Sound Engineers

Industry/Entity Type

Business

Requirements
Must have
• Refer to the current splash page – www.convene-expo.com
This is the look and feel we have developed for our brochure. We want to expand on this and create a professional corporate look and feel without alienating existing sound, light and vision sectors.

The website's focus is to register visitors to attend the show. Please include a floating 'Register Free' Call to action. Please also include floating social media buttons. For what I mean by 'floating' check out the Social media buttons on this website: http://quiverloop.com/2012/02/19/tall-hats-preview/ (scroll down to see effect).

We'll like to include a Rotating Banner at the top.

Sponsor element at the bottom off the page.

Sign up form functionality

Menu to be: About the Show, What's On, Register, How to Exhibit, Blog, Contact us.

I would like to see designs for a content page as well as the homepage.

```html
<!DOCTYPE html>
<html lang="en">
<head>
<meta charset="utf-8">
<title>Convene 2012 – Sound, Light, Vision</title>
<link rel="stylesheet" href="https://fonts.googleapis.com/css2?family=Questrial&family=Arimo:wght@400;700&family=Ubuntu:wght@700&display=swap">
<style>
:root{
  --ink:#222;
  --grey:#6f6f6f;
  --light-grey:#8a8a8a;
  --red:#e2001a;
  --blue:#6d9cbd;
  --yellow:#f2e31b;
  --yellow-dark:#d9c500;
  --panel:rgba(40,38,40,.86);
  --black:#0b0b0b;
}
*{margin:0;padding:0;box-sizing:border-box}
html,body{width:1200px;height:1125px;overflow:hidden;background:#fff}
body{position:relative;font-family:"Questrial",sans-serif;color:var(--grey)}
.header{position:absolute;left:0;top:0;width:1200px;height:102px;background:linear-gradient(#fff,#ececec);border-bottom:3px solid var(--red)}
.brand{position:absolute;left:150px;top:40px;display:flex;align-items:center;gap:8px}
.brand-mark{width:12px;height:12px;border-radius:50%;background:var(--red)}
.brand-name{font-size:32px;color:var(--ink);letter-spacing:-.5px}
.partner{position:absolute;left:303px;top:52px;font-size:15px;color:var(--ink)}
.nav{position:absolute;right:149px;top:68px;display:flex;gap:15px;font-size:16.5px;letter-spacing:.3px;font-family:"Arimo",sans-serif}
.nav a{color:var(--grey);text-decoration:none;position:relative}
.nav a.active::after{content:"";position:absolute;left:50%;top:25px;margin-left:-4px;border:4px solid transparent;border-bottom-color:var(--red)}
.banner{position:absolute;left:150px;top:132px;width:901px;height:360px;background:linear-gradient(160deg,#c9cdd8 0%,#8e8a95 35%,#a7784a 62%,#3b3230 100%);box-shadow:0 1px 2px rgba(0,0,0,.4)}
.banner-panel{position:absolute;left:502px;top:62px;width:398px;height:237px;background:var(--panel)}
.banner-date{position:absolute;left:0;top:30px;width:100%;text-align:center;color:#fff;font-size:21px;line-height:28px;letter-spacing:.3px}
.banner-arrows{position:absolute;left:44px;top:155px}
.cta{position:absolute;left:154px;top:158px;width:192px;height:48px;border-radius:3px;background:linear-gradient(var(--yellow),var(--yellow-dark));font-family:"Ubuntu",sans-serif;font-size:22px;letter-spacing:1.2px;color:#2a2a2a;display:flex;align-items:center;justify-content:center}
.col{position:absolute;top:520px}
.col-heading{font-size:16px;line-height:19px;text-transform:uppercase;color:var(--grey)}
.rule{height:3px;background:#333;position:absolute}
.sector-list{position:absolute;left:150px;top:593px;list-style:none;font-size:12px;line-height:23.4px;text-transform:uppercase}
.sector-list li::before{content:"•";margin:0 6px 0 5px}
.tick-grid{position:absolute;left:425px;top:588px;display:grid;grid-template-columns:136px 140px;row-gap:6px;font-size:11.5px;text-transform:uppercase;color:#222}
.tick{display:flex;align-items:center;gap:6px;height:17px}
.col-lead{position:absolute;left:745px;top:516px;font-size:19.5px;line-height:21px;text-transform:uppercase;color:var(--blue)}
.info-box{position:absolute;left:745px;top:612px;width:305px;height:110px;background:var(--black);color:#fff;font-family:"Arimo",sans-serif;font-size:9.5px;line-height:14.6px;padding:10px 10px;text-transform:uppercase;letter-spacing:.25px}
.sponsors{position:absolute;left:150px;top:747px;width:901px;height:137px;background:linear-gradient(#fff,#e2e2e2);box-shadow:1px 1px 2px rgba(0,0,0,.25);display:flex;justify-content:space-around;align-items:center;padding:0 10px}
.sponsor{display:flex;align-items:center;gap:6px;font-size:22px;color:var(--ink)}
.sponsor .dot{width:9px;height:9px;border-radius:50%;background:var(--red)}
.sponsor.partner-name{font-size:16px}
.footer{position:absolute;left:150px;top:955px;font-family:"Arimo",sans-serif;font-size:9px;line-height:14.6px;letter-spacing:.5px;text-transform:uppercase;color:var(--light-grey)}
</style>
</head>
<body>
<header class="header">
  <div class="brand"><span class="brand-mark"></span><span class="brand-name">Convene</span></div>
  <div class="partner">Meridian AV Guild</div>
  <nav class="nav">
    <a class="active" href="#">About the Show</a>
    <a href="#">What's On</a>
    <a href="#">Register</a>
    <a href="#">How to Exhibit</a>
    <a href="#">Blog</a>
    <a href="#">Contact us</a>
  </nav>
</header>

<section class="banner" role="img" aria-label="Harbour at dusk with the opera house sails and arch bridge">
  <div class="banner-panel">
    <p class="banner-date">21ST-23RD AUGUST 2012<br>HARBOURSIDE EXHIBITION<br>HALL, COCKLE QUAY</p>
    <svg class="banner-arrows" width="84" height="62" viewBox="0 0 84 62" aria-hidden="true">
      <path d="M4 6 L38 31 L4 56 M28 6 L62 31 L28 56 M50 14 L72 31 L50 48" fill="none" stroke="var(--yellow)" stroke-width="5" stroke-linecap="round" stroke-linejoin="round"/>
    </svg>
    <div class="cta">REGISTER FREE</div>
  </div>
</section>

<div class="col" style="left:150px;top:529px">
  <h2 class="col-heading">Descover the lates<br>investments in.....</h2>
</div>
<div class="rule" style="left:150px;top:580px;width:199px"></div>
<ul class="sector-list">
  <li>Concert Production</li>
  <li>AV Installation</li>
  <li>Broadcast</li>
  <li>Staging</li>
  <li>Lighting &amp; Entertainment Technology</li>
  <li>Digital Media &amp; Information Services</li>
</ul>

<div class="col" style="left:425px;top:521px">
  <h2 class="col-heading">Be part of Australia‘s only<br>event for the audio visual &amp; en-<br>tertaiment industry</h2>
</div>
<div class="rule" style="left:425px;top:579px;width:287px"></div>
<div class="tick-grid">
  <div class="tick"><svg width="14" height="14" viewBox="0 0 14 14"><circle cx="7" cy="7" r="6.5" fill="var(--red)"/><path d="M4 7.2 L6.2 9.4 L10 5" fill="none" stroke="#fff" stroke-width="1.6"/></svg>New Locations</div>
  <div class="tick"><svg width="14" height="14" viewBox="0 0 14 14"><circle cx="7" cy="7" r="6.5" fill="var(--red)"/><path d="M4 7.2 L6.2 9.4 L10 5" fill="none" stroke="#fff" stroke-width="1.6"/></svg>Even Bigger Show</div>
  <div class="tick"><svg width="14" height="14" viewBox="0 0 14 14"><circle cx="7" cy="7" r="6.5" fill="var(--red)"/><path d="M4 7.2 L6.2 9.4 L10 5" fill="none" stroke="#fff" stroke-width="1.6"/></svg>New Seminars</div>
  <div class="tick"><svg width="14" height="14" viewBox="0 0 14 14"><circle cx="7" cy="7" r="6.5" fill="var(--red)"/><path d="M4 7.2 L6.2 9.4 L10 5" fill="none" stroke="#fff" stroke-width="1.6"/></svg>Even Mor Surpises</div>
</div>

<h2 class="col-lead">Australia‘s largest<br>audio visual, entertainment &amp;<br>information communications<br>technology event</h2>
<div class="info-box">With over 500 brands on display, Convene in associ-ation with Meridian AV Guild, brings together the worlds of ICT, integrating all areas including visual, education, entertainment, audio &amp; lighting technology, worship, digital signage and unified communications.</div>

<section class="sponsors" aria-label="Sponsors">
  <div class="sponsor"><span class="dot"></span>Convene</div>
  <div class="sponsor partner-name">Meridian AV Guild</div>
  <div class="sponsor"><span class="dot"></span>Convene</div>
  <div class="sponsor partner-name">Meridian AV Guild</div>
  <div class="sponsor"><span class="dot"></span>Convene</div>
</section>

<footer class="footer">
  Strictly trade only. Entry is restricted to members of the ICT, audio visual and entertainment industries.<br>
  Persons not in these categories, including children will not be admitted at any time.<br>
  © 2011 Harbourline Exhibitions, Australia. All rights reserved. Level 2, 118 Wharf Lane, Sydney, NSW 2000, Australia.<br>
  Telephone: +61 2 5550 1400. Facsimile: +61 2 5550 1499.
</footer>
</body>
</html>
```